THE SILVER HEARTH SESSIONS - CD COVER DESIGN

I am a professional female vocalist based in Devon, UK. I require a CD COVER for a CHRISTMAS album of mixed genre tracks - jazz/big-band/country/gospel/acoustic songs, all with a traditional 'Festive/Christmas' theme.

Cover to fit STANDARD CD JEWEL CASE comprising: FRONT COVER INLAY / INSIDE FRONT / REAR INLAY and SPINE. Plus CD FACE.

The design needs to incorporate the 2 publicity photographs attached. CD1 (wearing WHITE FUR JACKET) is the main picture and preferred choice for front cover pic. CD2 (wearing RED DRESS) can be used anywhere in the design.

CD WORDING: Please see attached info. The track listing is also provided on a separate sheet.

Sick

Target Market(s)

Festive music market!

Industry/Entity Type

It Professional

Font styles to use
Serif
Sans Serif
Decorative
Script

Colors
ec1f27

Requirements
Must have
• CHRISTMAS / FESTIVE THEME!
• Must incorporate the 2 publicity photographs attached.
• TRACK LISTING to feature on CD FACE and REAR INLAY.
• CD WORDING attached.
Should not have
• Not keen on 'cartoon type' images - prefer more traditional.

```html
<!DOCTYPE html>
<html lang="en">
<head>
<meta charset="utf-8">
<title>The Silver Hearth Sessions – CD Package</title>
<link rel="stylesheet" href="https://fonts.googleapis.com/css2?family=Cinzel:wght@600;700&family=Marcellus&family=Open+Sans:wght@400;600;700&display=swap">
<style>
  :root {
    --board: #5a5a5a;
    --red: #ec1f27;
    --red-deep: #b3121a;
    --red-dark: #7d0b10;
    --gold: #e2b64a;
    --gold-light: #f6dc86;
    --white: #ffffff;
    --ink: #c8121a;
    --pine: #1f4a2a;
  }
  * { box-sizing: border-box; margin: 0; padding: 0; }
  html, body { width: 1200px; height: 1074px; overflow: hidden; background: var(--board); }
  body { position: relative; font-family: "Open Sans", Arial, sans-serif; }

  .panel { position: absolute; overflow: hidden; }

  /* Inside front inlay */
  .inside-front {
    left: 58px; top: 43px; width: 554px; height: 477px;
    background: radial-gradient(ellipse at 70% 30%, var(--red) 0%, var(--red-deep) 55%, var(--red-dark) 100%);
  }
  .bauble-art {
    position: absolute; left: 0; top: 0; width: 260px; height: 477px;
    background: radial-gradient(circle at 40% 45%, rgba(255,255,255,0.10), rgba(0,0,0,0.18) 70%, transparent 71%);
  }
  .bio { position: absolute; left: 134px; top: 192px; width: 400px; color: var(--white); font-size: 12.5px; line-height: 1.35; }
  .bio strong { font-weight: 700; }
  .member { margin-top: 14px; font-weight: 700; }
  .guild-mark { display: flex; align-items: center; gap: 7px; margin-top: 10px; font-size: 20px; font-weight: 700; }
  .guild-mark .dot { width: 14px; height: 14px; border-radius: 50%; background: var(--white); }
  .booking { margin-top: 14px; font-weight: 700; }
  .booking p { font-weight: 700; }
  .booking span { font-weight: 400; }
  .social { display: flex; gap: 6px; margin-top: 10px; }
  .social i { width: 20px; height: 20px; border-radius: 50%; background: var(--white); display: block; }

  /* CD face */
  .disc {
    left: 634px; top: 12px; width: 532px; height: 532px; border-radius: 50%;
    background: #f4f1ee;
  }
  .disc-photo {
    position: absolute; left: 0; top: 0; width: 320px; height: 532px;
    background: linear-gradient(160deg, #f7f3ee 0%, #efe2c8 35%, #c4161d 70%, #9e0f15 100%);
  }
  .disc-tracks { position: absolute; left: 318px; top: 70px; width: 190px; text-align: center; color: var(--ink); }
  .disc-tracks h3 { font-family: "Marcellus", serif; font-weight: 400; font-size: 15px; letter-spacing: 1px; margin-bottom: 8px; }
  .disc-tracks li { list-style: none; font-size: 7.6px; line-height: 11.6px; }
  .disc-band {
    position: absolute; left: 0; top: 342px; width: 532px; height: 110px;
    background: linear-gradient(90deg, rgba(125,11,16,0.9), rgba(190,20,27,0.92) 50%, rgba(125,11,16,0.9));
    text-align: center;
  }
  .disc-band .title { font-family: "Cinzel", serif; font-weight: 700; color: var(--gold); font-size: 29px; line-height: 31px; padding-top: 12px; }
  .disc-band .artist { margin: 6px auto 0; width: 250px; display: flex; align-items: center; gap: 8px; color: var(--white); font-size: 14px; letter-spacing: 1.5px; }
  .disc-band .artist::before, .disc-band .artist::after { content: ""; flex: 1; height: 1px; background: var(--white); }
  .disc-hole { position: absolute; left: 200px; top: 200px; width: 132px; height: 132px; border-radius: 50%; border: 1px solid rgba(255,255,255,0.9); background: rgba(255,255,255,0.25); }
  .disc-hole::after { content: ""; position: absolute; left: 19px; top: 19px; width: 92px; height: 92px; border-radius: 50%; background: var(--board); }

  /* Rear inlay + spine + front */
  .rear { left: 58px; top: 553px; width: 530px; height: 459px;
    background: radial-gradient(ellipse at 55% 45%, var(--red) 0%, var(--red-deep) 70%, var(--red-dark) 100%); }
  .garland-top { position: absolute; left: 0; top: 0; width: 230px; height: 270px;
    background: linear-gradient(135deg, var(--pine), rgba(31,74,42,0.55) 55%, transparent 75%); }
  .garland-bottom { position: absolute; right: 0; bottom: 0; width: 300px; height: 330px;
    background: linear-gradient(315deg, var(--pine), rgba(31,74,42,0.55) 50%, transparent 72%); }
  .rear h2 { position: absolute; right: 52px; top: 34px; font-family: "Marcellus", serif; font-weight: 400; color: var(--white); font-size: 26px; line-height: 30px; text-align: right; letter-spacing: 0.5px; }
  .rear ol { list-style: none; position: absolute; color: var(--white); font-size: 11.5px; line-height: 17px; }
  .tracks-a { right: 53px; top: 100px; text-align: right; }
  .tracks-b { left: 67px; top: 262px; }

  .spine { left: 588px; top: 553px; width: 24px; height: 459px; background: var(--red-deep);
    writing-mode: vertical-rl; display: flex; align-items: center; padding-top: 12px; }
  .spine .title { font-family: "Cinzel", serif; font-weight: 700; color: var(--gold); font-size: 14px; letter-spacing: 0.5px; }
  .spine .artist { margin-top: 24px; color: var(--white); font-size: 11px; letter-spacing: 1px; }

  .front { left: 612px; top: 553px; width: 528px; height: 459px;
    background: linear-gradient(180deg, #3d1a12 0%, #6a2218 35%, #e9e0d8 65%, #f5f1ec 100%); }
  .front-photo { position: absolute; inset: 0;
    background: radial-gradient(ellipse at 50% 45%, #f3e6cf 0%, #d9c49e 30%, rgba(90,30,20,0.2) 60%, transparent 80%); }
  .front-band { position: absolute; left: 0; top: 334px; width: 528px; height: 86px;
    background: linear-gradient(90deg, rgba(110,10,14,0.85), rgba(170,18,25,0.9) 50%, rgba(110,10,14,0.85)); text-align: center; }
  .front-band .title { font-family: "Cinzel", serif; font-weight: 700; color: var(--gold); font-size: 33px; padding-top: 6px; line-height: 40px; }
  .front-band .artist { color: var(--white); font-size: 24px; letter-spacing: 2.5px; font-weight: 400; line-height: 30px; }
</style>
</head>
<body>

<section class="panel inside-front">
  <div class="bauble-art" role="img" aria-label="Hanging glass Christmas baubles"></div>
  <div class="bio">
    <p><strong>HOLLY MARLOWE</strong> is a British PROFESSIONAL SINGER and award winning International MULTI-TRIBUTE ARTISTE. Available for bookings in the UK &amp; WORLDWIDE.</p>
    <p class="member">Member of PERFORMERS GUILD.</p>
    <div class="guild-mark"><span class="dot"></span>Guild</div>
    <div class="booking">
      <p>BOOKING ENQUIRIES:</p>
      <p>Telephone: <span>&nbsp;07700 900 412</span></p>
      <p>Email: <span>&nbsp;hollymarlowe@example.com</span></p>
    </div>
    <div class="social"><i></i><i></i><i></i><i></i><i></i><i></i><i></i></div>
  </div>
</section>

<section class="panel disc">
  <div class="disc-photo" role="img" aria-label="Publicity photo of the singer in a red dress"></div>
  <div class="disc-tracks">
    <h3>SONGS</h3>
    <ol>
      <li>01. JINGLE BELLS</li>
      <li>02. HARK THE HERALD ANGELS SING</li>
      <li>03. DO YOU HEAR WHAT I HEAR</li>
      <li>04. WINTER WONDERLAND</li>
      <li>05. I'VE GOT MY LOVE TO KEEP ME WARM</li>
      <li>06. THE FIRST NOEL</li>
      <li>07. LITTLE DRUMMER BOY</li>
      <li>08. BABY ITS COLD OUTSIDE</li>
      <li>09. TENNESSEE CHRISTMAS</li>
      <li>10. HAVE A HOLLY JOLLY CHRISTMAS</li>
      <li>11. SANTA BABY</li>
      <li>12. BLUE CHRISTMAS</li>
      <li>13. THE CHRISTMAS SONG</li>
      <li>14. O COME ALL YE FAITHFUL</li>
      <li>15. HAVE YOURSELF A MERRY<br>LITTLE CHRISTMAS</li>
      <li>16. LET IT SNOW</li>
      <li>17. IN THE BLEAK MIDWINTER</li>
      <li>18. MARY'S BOY CHILD</li>
      <li>19. WHITE CHRISTMAS</li>
    </ol>
  </div>
  <div class="disc-band">
    <div class="title">THE SILVER HEARTH<br>SESSIONS</div>
    <div class="artist">HOLLY MARLOWE</div>
  </div>
  <div class="disc-hole"></div>
</section>

<section class="panel rear">
  <div class="garland-top" role="img" aria-label="Pine garland with gold snowflakes and stars"></div>
  <div class="garland-bottom" role="img" aria-label="Pine garland with baubles and gold snowflakes"></div>
  <h2>SONGS FOR THE<br>FESTIVE SEASON</h2>
  <ol class="tracks-a">
    <li>01. JINGLE BELLS</li>
    <li>02. HARK THE HERALD ANGELS SING</li>
    <li>03. DO YOU HEAR WHAT I HEAR</li>
    <li>04. WINTER WONDERLAND</li>
    <li>05. I'VE GOT MY LOVE TO KEEP ME WARM</li>
    <li>06. THE FIRST NOEL</li>
    <li>07. LITTLE DRUMMER BOY</li>
    <li>08. BABY ITS COLD OUTSIDE</li>
    <li>09. TENNESSEE CHRISTMAS</li>
    <li>10. HAVE A HOLLY JOLLY CHRISTMAS</li>
  </ol>
  <ol class="tracks-b">
    <li>11. SANTA BABY</li>
    <li>12. BLUE CHRISTMAS</li>
    <li>13. THE CHRISTMAS SONG</li>
    <li>14. O COME ALL YE FAITHFUL</li>
    <li>15. HAVE YOURSELF A MERRY LITTLE CHRISTMAS</li>
    <li>16. LET IT SNOW</li>
    <li>17. IN THE BLEAK MIDWINTER</li>
    <li>18. MARY'S BOY CHILD</li>
    <li>19. WHITE CHRISTMAS</li>
    <li>20. SANTA CLAUS IS COMIN' IN A BOOGIE<br>WOOGIE CHOO-CHOO TRAIN</li>
  </ol>
</section>

<section class="panel spine">
  <span class="title">THE SILVER HEARTH SESSIONS</span>
  <span class="artist">HOLLY MARLOWE</span>
</section>

<section class="panel front">
  <div class="front-photo" role="img" aria-label="Publicity photo of the singer in a white fur jacket before a decorated Christmas tree"></div>
  <div class="front-band">
    <div class="title">THE SILVER HEARTH SESSIONS</div>
    <div class="artist">HOLLY MARLOWE</div>
  </div>
</section>

</body>
</html>
```